Marina Holt 2014 Calendar

We need a 12 month, wall hanging Calendar design featuring the actress Marina Holt. It is a product for her fans and the feel of this years photographs is very otherworldly with saturated colors and the incorporation of elements such as fire, ice and water. We are looking for bold, graphic designs to support and reflect this feel. There is a very tight schedule for the completion of this calendar as it needs to go into production asap so any designers submitting concepts should have the ability and enthusiasm to dedicate the necessary time required to get this product to the printers quickly.
We have included three of the twelve photographs for you to use with a combination of vertical and horizontal images. Once the design is selected we will provide the remaining nine photos to be incorporated. These images are to be kept completely confidential please.
Thank you and we are looking forward to seeing your ideas!!
Requirements
Must have
- Bio about Marina Holt, crédits for art director, photographer etc. Some negative space on cover so that it maybe autographed by actress. 12 months reflected in page design.

```html
<!DOCTYPE html>
<html lang="en">
<head>
<meta charset="utf-8">
<title>Marina Holt 2014 Calendar – January</title>
<link href="https://fonts.googleapis.com/css2?family=Ubuntu:wght@400;500&display=swap" rel="stylesheet">
<style>
:root{
  --ice-deep:#0d2a4a;
  --ice-mid:#3f6f9c;
  --ice-light:#c9dcec;
  --panel:rgba(235,242,250,0.72);
  --ink:#14305a;
  --accent:#2f5f9e;
  --cell:#7f9cc4;
  --cell-border:rgba(255,255,255,0.85);
  --white:#ffffff;
}
*{margin:0;padding:0;box-sizing:border-box}
html,body{width:849px;height:1200px;overflow:hidden;background:#fff}
.page{position:relative;width:849px;height:1200px;overflow:hidden;font-family:"Ubuntu",sans-serif}
.photo{position:absolute;inset:0;
  background:
    radial-gradient(ellipse at 48% 40%, rgba(230,225,235,0.55) 0%, rgba(160,150,170,0.35) 22%, transparent 45%),
    radial-gradient(ellipse at 85% 30%, rgba(240,245,255,0.9) 0%, transparent 40%),
    linear-gradient(90deg, var(--ice-deep) 0%, var(--ice-mid) 35%, #a9c3dc 65%, var(--ice-light) 100%);}
.name{position:absolute;left:20px;top:14px;color:var(--white);font-size:46px;font-weight:400;letter-spacing:0.5px}
.panel{position:absolute;left:0;top:680px;width:849px;height:438px;background:var(--panel)}
.month{position:absolute;left:26px;top:694px;color:var(--ink);font-size:48px;font-weight:400;letter-spacing:0.5px}
.weekdays{position:absolute;left:23px;top:752px;display:grid;grid-template-columns:repeat(7,58px);column-gap:4px;color:var(--ink);font-size:26px}
.weekdays span{text-align:center;white-space:nowrap}
.grid{position:absolute;left:23px;top:790px;display:grid;grid-template-columns:repeat(7,58px);grid-auto-rows:58px;gap:4px}
.day{background:var(--cell);border:2px solid var(--cell-border);color:var(--white);font-size:27px;display:flex;align-items:center;justify-content:center}
.day.other{opacity:0.8}
.bio{position:absolute;left:492px;top:790px;width:340px;color:var(--accent)}
.bio h2{font-size:30px;font-weight:400;margin-bottom:14px;color:var(--accent)}
.bio p{font-size:24px;line-height:29px}
</style>
</head>
<body>
<div class="page">
  <div class="photo" role="img" aria-label="Portrait of the actress in a sparkling sequinned gown against a frosted blue winter forest"></div>
  <h1 class="name">Marina Holt</h1>
  <div class="panel"></div>
  <div class="month">JANUARY 2014</div>
  <div class="weekdays"><span>Mon</span><span>Tue</span><span>Wed</span><span>Thu</span><span>Fri</span><span>Sat</span><span>Sun</span></div>
  <div class="grid">
    <div class="day other">30</div><div class="day other">31</div><div class="day">1</div><div class="day">2</div><div class="day">3</div><div class="day">4</div><div class="day">5</div>
    <div class="day">6</div><div class="day">7</div><div class="day">8</div><div class="day">9</div><div class="day">10</div><div class="day">11</div><div class="day">12</div>
    <div class="day">13</div><div class="day">14</div><div class="day">15</div><div class="day">16</div><div class="day">17</div><div class="day">18</div><div class="day">19</div>
    <div class="day">20</div><div class="day">21</div><div class="day">22</div><div class="day">23</div><div class="day">24</div><div class="day">25</div><div class="day">26</div>
    <div class="day">27</div><div class="day">28</div><div class="day">29</div><div class="day">30</div><div class="day">31</div><div class="day other">1</div><div class="day other">2</div>
  </div>
  <div class="bio">
    <h2>Some text about Marina</h2>
    <p>Lorem ipsum dolor sit amet, cu sea minim albucius, fugit malorum et mea. Omnium propriae ad has, latine eligendi iudicabit nam no.</p>
  </div>
</div>
</body>
</html>
```